A new website for Electrical Contractor Business

We are looking for a unique and new WordPress website design which would include 5 Pages - Home Page, Meet the Team, Our Services, Our Projects and Contact Us page.

The global theme for the website needs to be professional but simple to navigate as we cater for both business and home owner customers.

Our core business service is targeted around lighting from single room decorative to large office so the theme should incorporate this in some way.

The home page should include;
Our business logo, Contact number, Email address, small Image rotation box - Highlighting pervious projectsText box - With welcome message, chirpnet feed news reel/Customer feed back box.

I would also like to see a 2 boxes for the separate customer types we services. Business and Home Owner. each box will have a small image with a small text description with a link to the area of the services page relevant to that customer type.

Meet the team page -This will be introducing potential customers to the team so I would like it to include for each team member. Something like a small image and text area which will introduce an outline of the team members skills and abilities.

Our Services page This page will be outlining the different services on offer to the both customer types business and homeowner. Each service should have an image with text description of the service would good here.

Our projects page-Will include images of pervious projects and work we have completed along with a text area for the project description/ outliner.

Contact Us page - Should include a contact form which should include an option for the customer to quest us to call them back, also a selection box for them to inform us our how they found our details would be good.

Colour - The theme colours can be taken from the logo or feel free to impress with your own imagination.

Remember we are looking for a website that will interest our customers enough to except our services or be drawn further into the website.. So call to action links to other areas of the site/ contact page are welcome

Target Market(s)

Business - Office, warehousing and Large Store - lighting and Power
Home owner lighting and power

Coding

Coded - Design and coding required

Number of Pages Required

5+ page

Font styles to use
Serif
Sans Serif

Colors

Designer to choose colors to be used in the design.

Requirements
Must have
• Logo integrated into the website design - i.e. website colours which allow the logo to blend into the design.
Nice to have
• Custom but professional theme catering to business customers, but also show that we do provide services to home owners too.
Should not have
• Sorry am not interested in one oversized block image on rotation covering half the home page.. Images will be needed but not a single block over sized frame with not text, shape. Please use your imagination when considering this design

```html
<!DOCTYPE html>
<html lang="en">
<head>
<meta charset="utf-8">
<title>Brightway Systems — Electrical Contractors</title>
<link href="https://fonts.googleapis.com/css2?family=Arimo:wght@400;700&family=Open+Sans:wght@400;600&display=swap" rel="stylesheet">
<style>
:root{
  --orange:#e8652a;
  --orange-dark:#c94f1c;
  --navy:#1f3266;
  --navy-deep:#18284f;
  --ink:#333333;
  --muted:#555555;
  --line:#dddddd;
  --white:#ffffff;
  --paper:#ffffff;
}
*{margin:0;padding:0;box-sizing:border-box}
html,body{width:1200px;height:4500px;overflow:hidden;background:var(--paper)}
body{position:relative;font-family:"Open Sans",Arial,sans-serif;color:var(--ink)}
.abs{position:absolute}
h1,h2,h3,h4{font-family:"Arimo",Arial,sans-serif;font-weight:700}
.brand{display:flex;align-items:center;gap:16px;font-family:"Arimo",Arial,sans-serif;font-weight:700;color:var(--navy)}
.brand-dot{border-radius:50%;background:var(--orange)}

/* header */
.site-header{top:0;left:0;width:1200px;height:120px}
.site-header .brand{left:90px;top:30px;font-size:30px}
.site-header .brand-dot{width:60px;height:60px}
.contact-chip{display:flex;gap:18px;align-items:center;top:30px}
.chip-icon{width:48px;height:48px;background:var(--orange);border-radius:6px;display:flex;align-items:center;justify-content:center}
.chip-text{font-family:"Arimo",Arial,sans-serif;line-height:1.3}
.chip-text .label{font-size:22px;color:var(--ink)}
.chip-text .value{font-size:21px;font-weight:700;color:var(--orange)}

.main-nav{top:120px;left:0;width:1200px;height:75px;border-top:1px solid var(--line);border-bottom:1px solid var(--line);display:flex;justify-content:center;gap:0}
.main-nav a{font-family:"Arimo",Arial,sans-serif;font-size:20px;color:var(--ink);text-decoration:none;line-height:75px;padding:0 56px}
.main-nav a.active{color:var(--orange)}

/* hero */
.hero{top:195px;left:0;width:1200px;height:585px;background:linear-gradient(120deg,#3b4a5c 0%,#6d7a86 35%,#8b9aa8 60%,#4c5a6b 100%)}
.hero-shade{inset:0;background:rgba(20,30,50,.35)}
.hero h1{top:120px;left:0;width:1200px;text-align:center;color:var(--white);font-size:56px;line-height:68px}
.hero p{top:264px;left:180px;width:840px;text-align:center;color:var(--white);font-size:24px;line-height:32px}
.hero .btn-outline{top:393px;left:495px;width:204px;height:57px;border:2px solid var(--white);color:var(--white);font-family:"Arimo",Arial,sans-serif;font-size:26px;line-height:53px;text-align:center}
.hero-arrow{top:414px;width:48px;height:48px;border-radius:50%;background:var(--white);display:flex;align-items:center;justify-content:center}
.hero-notch{top:500px;left:540px;width:120px;height:85px}

/* welcome */
.welcome h2{top:890px;left:300px;width:780px;text-align:center;color:var(--orange);font-size:44px}
.welcome-photo{top:945px;left:102px;width:306px;height:306px;border-radius:50%;background:radial-gradient(circle,#ffffff 0 32%,#9aa7b5 33% 60%,#3d4f66 61% 100%)}
.welcome p{top:1010px;left:447px;width:650px;font-size:17px;line-height:30px;color:var(--muted)}

/* projects */
.projects-band{top:1314px;left:0;width:1200px;height:411px;background:linear-gradient(180deg,var(--navy-deep),var(--navy))}
.projects-band h2{top:48px;left:0;width:1200px;text-align:center;color:var(--white);font-size:42px}
.projects-band p{top:118px;left:250px;width:700px;text-align:center;color:#dde3ef;font-size:17px;line-height:28px}
.project-card{top:1584px;width:330px}
.project-card .thumb{height:195px;border-radius:6px}
.project-card h3{margin-top:24px;text-align:center;color:var(--orange);font-size:25px}
.project-card p{margin-top:12px;text-align:center;font-size:16px;line-height:24px;color:var(--muted)}
.dots{top:1950px;left:570px;display:flex;gap:6px}
.dots span{width:15px;height:15px;border-radius:50%;background:var(--navy)}
.dots span.on{background:var(--orange)}

/* feeds */
.feed-title{top:2040px;color:var(--orange);font-size:42px}
.tweet-box{top:2145px;left:90px;width:441px;height:435px;border:1px solid var(--line);box-shadow:0 2px 8px rgba(0,0,0,.12);overflow:hidden}
.tweet-box .head{position:absolute;top:18px;left:18px;font-family:"Arimo",Arial,sans-serif;font-weight:700;color:#2a7fd4;font-size:18px}
.tweet-box .rule{position:absolute;top:50px;left:0;width:420px;border-top:1px solid var(--line)}
.tweet-box .avatar{position:absolute;top:80px;left:18px;width:66px;height:66px;border-radius:50%;background:var(--navy)}
.tweet-box .who{position:absolute;top:86px;left:100px;font-family:"Arimo",Arial,sans-serif;font-weight:700;color:var(--orange);font-size:18px}
.tweet-box .handle{position:absolute;top:112px;left:100px;font-size:14px;color:var(--muted)}
.tweet-box .body{position:absolute;top:162px;left:18px;width:390px;font-size:14px;line-height:21px;color:var(--muted)}
.tweet-box .media{position:absolute;top:306px;left:18px;width:380px;height:96px;background:linear-gradient(90deg,#6c7a8c,#2c2f6a 55%,#9aa2b0)}
.tweet-box .scroll{position:absolute;top:0;right:0;width:21px;height:435px;background:#eeeeee}
.tweet-box .thumbbar{position:absolute;top:12px;right:4px;width:12px;height:400px;background:var(--orange)}
.news-item{left:621px;width:500px;height:130px}
.news-item .thumb{position:absolute;left:0;top:0;width:150px;height:126px;background:linear-gradient(135deg,#9aa4ae,#5a6470)}
.news-item h4{position:absolute;left:177px;top:6px;font-size:19px;color:var(--ink)}
.news-item .meta{position:absolute;left:177px;top:40px;display:flex;gap:44px;font-size:15px;color:var(--ink);align-items:center}
.news-item .meta span{display:flex;align-items:center;gap:10px}
.news-item p{position:absolute;left:177px;top:72px;width:330px;font-size:15px;line-height:21px;color:var(--muted)}

/* feedback */
.feedback-band{top:2715px;left:0;width:1200px;height:525px;background:linear-gradient(135deg,var(--orange),var(--orange-dark))}
.feedback-band h2{top:48px;left:0;width:1200px;text-align:center;color:var(--white);font-size:46px}
.quote-card{width:306px;height:180px;background:var(--white);border-radius:12px;box-shadow:0 4px 12px rgba(0,0,0,.18)}
.quote-card p{position:absolute;top:54px;left:24px;width:258px;text-align:center;font-size:14px;line-height:21px;color:var(--muted)}
.quote-card .tail{position:absolute;bottom:-14px;left:139px;width:28px;height:28px;background:var(--white);transform:rotate(45deg)}
.avatar-ring{width:102px;height:102px;border-radius:50%;border:4px solid var(--white);background:linear-gradient(160deg,#c99a7a,#6b4b3a)}
.quote-name{width:306px;text-align:center;color:var(--white);font-family:"Arimo",Arial,sans-serif;font-size:20px;line-height:24px}

/* service types */
.types h2{top:3300px;left:0;width:1200px;text-align:center;color:var(--orange);font-size:44px}
.types .intro{top:3378px;left:240px;width:720px;text-align:center;font-size:18px;line-height:30px;color:var(--ink)}
.type-card{top:3516px;width:411px;height:516px;background:var(--navy)}
.type-card .thumb{height:234px}
.type-card h3{margin-top:30px;text-align:center;color:var(--white);font-size:34px}
.type-card p{margin:16px auto 0;width:340px;text-align:center;color:var(--white);font-size:16px;line-height:26px}
.type-card .more{position:absolute;bottom:36px;left:0;width:411px;display:flex;justify-content:center;align-items:center;gap:18px;color:var(--white);font-family:"Arimo",Arial,sans-serif;font-size:22px}

/* newsletter */
.newsletter{top:4080px;left:0;width:1200px;height:105px;background:var(--orange)}
.newsletter h3{position:absolute;top:33px;left:90px;color:var(--white);font-weight:400;font-size:36px}
.newsletter .field{position:absolute;top:28px;left:438px;width:333px;height:51px;border:2px solid var(--white);color:var(--white);font-size:18px;line-height:47px;padding-left:12px}
.newsletter .cta{position:absolute;top:28px;left:900px;width:186px;height:51px;border:2px solid var(--white);color:var(--white);font-family:"Arimo",Arial,sans-serif;font-size:22px;line-height:47px;text-align:center}

/* footer */
.site-footer{top:4185px;left:0;width:1200px;height:315px;background:var(--navy)}
.site-footer .brand{position:absolute;left:90px;top:48px;flex-direction:column;gap:12px;color:var(--white);font-size:22px}
.site-footer .brand-dot{width:150px;height:150px;background:var(--white)}
.foot-col{position:absolute;top:60px;color:var(--white)}
.foot-col h4{font-size:27px;margin-bottom:18px}
.foot-col li{list-style:none;font-size:16px;line-height:24px}
.foot-bottom{position:absolute;top:268px;left:90px;width:1020px;display:flex;justify-content:space-between;align-items:center;color:var(--white);font-size:15px}
.social{display:flex;gap:18px}
.social span{width:24px;height:24px;background:var(--white);border-radius:3px}
</style>
</head>
<body>

<header class="site-header abs">
  <div class="brand abs"><span class="brand-dot"></span>Brightway Systems</div>
  <div class="contact-chip abs" style="left:471px">
    <div class="chip-icon"><svg width="26" height="26" viewBox="0 0 24 24"><path fill="#fff" d="M6.6 10.8a15 15 0 0 0 6.6 6.6l2.2-2.2c.3-.3.7-.4 1-.2 1.1.4 2.3.6 3.6.6.6 0 1 .4 1 1V20c0 .6-.4 1-1 1A17 17 0 0 1 3 4c0-.6.4-1 1-1h3.5c.6 0 1 .4 1 1 0 1.2.2 2.4.6 3.6.1.3 0 .7-.2 1z"/></svg></div>
    <div class="chip-text"><div class="label">Call Us Today</div><div class="value">01632 960418</div></div>
  </div>
  <div class="contact-chip abs" style="left:723px">
    <div class="chip-icon"><svg width="28" height="22" viewBox="0 0 28 22"><rect x="1" y="1" width="26" height="20" rx="2" fill="#fff"/><path d="M2 3l12 9 12-9" stroke="#e8652a" stroke-width="2.4" fill="none"/></svg></div>
    <div class="chip-text"><div class="label">Mail Us Today</div><div class="value">info@brightwaysystems.co.uk</div></div>
  </div>
</header>

<nav class="main-nav abs">
  <a class="active" href="#">HOME</a>
  <a href="#">MEET THE TEAM</a>
  <a href="#">OUR SERVICES</a>
  <a href="#">PROJECTS</a>
  <a href="#">CONTACT US</a>
</nav>

<section class="hero abs" role="img" aria-label="Photo of an electrician working on a wired control panel">
  <div class="hero-shade abs"></div>
  <h1 class="abs">Welcome to Brightway<br>Systems</h1>
  <p class="abs">Lorem ipsum dolor sit amet, consectetur adipiscing elit. Duis egestas sapien non libero eleifend facilisis. Donec consectetur aliquam tortor, nec viverra magna dictum nec.</p>
  <div class="btn-outline abs">View More</div>
  <div class="hero-arrow abs" style="left:21px"><svg width="20" height="20" viewBox="0 0 20 20"><path d="M13 3l-7 7 7 7" stroke="#1f3266" stroke-width="3" fill="none"/></svg></div>
  <div class="hero-arrow abs" style="left:1131px"><svg width="20" height="20" viewBox="0 0 20 20"><path d="M7 3l7 7-7 7" stroke="#1f3266" stroke-width="3" fill="none"/></svg></div>
  <svg class="hero-notch abs" viewBox="0 0 120 85"><path d="M0 85L60 25 120 85z" fill="#fff"/><circle cx="60" cy="62" r="20" fill="#e8652a"/></svg>
</section>

<section class="welcome">
  <h2 class="abs">Welcome to Brightway Systems</h2>
  <div class="welcome-photo abs" role="img" aria-label="Circular collage of lighting and wiring project photos"></div>
  <p class="abs">Lorem ipsum dolor sit amet, consectetur adipiscing elit. Duis egestas sapien non libero eleifend facilisis. Donec consectetur aliquam tortor, nec viverra magna dictum nec. Phasellus interdum lacus at ex placerat, non ultricies velit consectetur. Proin maximus ornare feugiat. In hac habitasse platea dictumst. Cras vel porta diam. Sed id efficitur ligula.Vestibulum ante ipsum primis in faucibus orci luctus et ultrices posuere cubilia Curae; Nam non laoreet dui. Ut nec venenatis nisl.</p>
</section>

<section class="projects-band abs">
  <h2 class="abs">Projects</h2>
  <p class="abs">Lorem ipsum dolor sit amet, consectetur adipiscing elit. Duis egestas sapien non libero eleifend facilisis. Donec consectetur aliquam tortor, nec viverra magna dictum nec.</p>
</section>
<article class="project-card abs" style="left:90px">
  <div class="thumb" role="img" aria-label="Technician testing a circuit board" style="background:linear-gradient(135deg,#5fb0d8,#2a6f9c)"></div>
  <h3>Lorem ipsum dolor</h3>
  <p>Lorem ipsum dolor sit amet, consectetur adipiscing elit. Nunc vel magna nunc. Pellentesque sed imperdiet risus.</p>
</article>
<article class="project-card abs" style="left:435px">
  <div class="thumb" role="img" aria-label="Electrician measuring a distribution board with a multimeter" style="background:linear-gradient(135deg,#8a8f96,#3c3f44)"></div>
  <h3>Lorem ipsum dolor</h3>
  <p>Lorem ipsum dolor sit amet, consectetur adipiscing elit. Nunc vel magna nunc. Pellentesque sed imperdiet risus.</p>
</article>
<article class="project-card abs" style="left:780px">
  <div class="thumb" role="img" aria-label="Engineer wiring a server cabinet" style="background:linear-gradient(135deg,#b7c3cc,#56697c)"></div>
  <h3>Lorem ipsum dolor</h3>
  <p>Lorem ipsum dolor sit amet, consectetur adipiscing elit. Nunc vel magna nunc. Pellentesque sed imperdiet risus.</p>
</article>
<div class="dots abs"><span></span><span></span><span class="on"></span></div>

<h2 class="feed-title abs" style="left:87px">chirpnet Feed</h2>
<h2 class="feed-title abs" style="left:621px">News Feed</h2>

<aside class="tweet-box abs">
  <div class="head">Posts</div>
  <div class="rule"></div>
  <div class="avatar"></div>
  <div class="who">Brightway Systems</div>
  <div class="handle">@brightwaysystems</div>
  <div class="body">It is a long established fact that a reader will be distracted by the readable content of a page when looking at its layout. Using plain filler gives a fair spread of letters, as opposed to using short repeated words here and there.</div>
  <div class="media" role="img" aria-label="Photo of electrical tools and cabling"></div>
  <div class="scroll"></div><div class="thumbbar"></div>
</aside>

<article class="news-item abs" style="top:2139px">
  <div class="thumb" role="img" aria-label="Electrician at a workbench"></div>
  <h4>Neque porro</h4>
  <div class="meta"><span>&#9679; Admin</span><span>&#9636; April 21 2019</span></div>
  <p>Lorem ipsum dolor sit amet, consectetur adipiscing elit. Praesent urna enim, ultrices non semper nec, tincidunt a urna.</p>
</article>
<article class="news-item abs" style="top:2310px">
  <div class="thumb" role="img" aria-label="Technician fitting a control unit"></div>
  <h4>Quisquam Est Qui</h4>
  <div class="meta"><span>&#9679; Admin</span><span>&#9636; April 21 2019</span></div>
  <p>Lorem ipsum dolor sit amet, consectetur adipiscing elit. Praesent urna enim, ultrices non semper nec, tincidunt a urna.</p>
</article>
<article class="news-item abs" style="top:2481px">
  <div class="thumb" role="img" aria-label="Engineer inspecting a panel"></div>
  <h4>Consectetur</h4>
  <div class="meta"><span>&#9679; Admin</span><span>&#9636; April 21 2019</span></div>
  <p>Lorem ipsum dolor sit amet, consectetur adipiscing elit. Praesent urna enim, ultrices non semper nec</p>
</article>

<section class="feedback-band abs">
  <h2 class="abs">Clients Feedback</h2>
  <div class="quote-card abs" style="left:99px;top:225px"><p>Lorem ipsum dolor sit amet, consectetur adipiscing elit. Praesent urna enim, ultrices non semper nec, tincidunt a urna. Morbi eleifend, lectus vel dignissim accumsan, massa turpis</p><div class="tail"></div></div>
  <div class="quote-card abs" style="left:444px;top:180px"><p>Lorem ipsum dolor sit amet, consectetur adipiscing elit. Praesent urna enim, ultrices non semper nec, tincidunt a urna. Morbi eleifend, lectus vel dignissim accumsan, massa turpis</p><div class="tail"></div></div>
  <div class="quote-card abs" style="left:792px;top:225px"><p>Lorem ipsum dolor sit amet, consectetur adipiscing elit. Praesent urna enim, ultrices non semper nec, tincidunt a urna. Morbi eleifend, lectus vel dignissim</p><div class="tail"></div></div>
  <div class="avatar-ring abs" style="left:201px;top:174px" role="img" aria-label="Client portrait"></div>
  <div class="avatar-ring abs" style="left:546px;top:147px" role="img" aria-label="Client portrait"></div>
  <div class="avatar-ring abs" style="left:894px;top:174px" role="img" aria-label="Client portrait"></div>
  <div class="quote-name abs" style="left:99px;top:441px">Marta P<br>April 28, 2019</div>
  <div class="quote-name abs" style="left:444px;top:405px">Nina K<br>April 19, 2018</div>
  <div class="quote-name abs" style="left:792px;top:441px">Sam T<br>April 17, 2019</div>
</section>

<section class="types">
  <h2 class="abs">Types Of Services</h2>
  <p class="intro abs">Lorem ipsum dolor sit amet, consectetur adipiscing elit. Duis egestas sapien non libero eleifend facilisis. Donec consectetur aliquam tortor, nec viverra magna dictum nec. Phasellus interdum lacus at ex placerat, non ultricies velit consectetur.</p>
  <article class="type-card abs" style="left:120px">
    <div class="thumb" role="img" aria-label="Engineers reviewing plans beside an industrial electrical installation" style="background:linear-gradient(135deg,#c9d2da,#7d8b98)"></div>
    <h3>Business</h3>
    <p>Lorem ipsum dolor sit amet, consectetur adipiscing elit. Duis egestas sapien non libero eleifend facilisis. Donec consectetur aliquam tortor, nec viverra magna dictum nec.</p>
    <div class="more">Read More <svg width="22" height="18" viewBox="0 0 22 18"><path d="M2 9h16M12 3l6 6-6 6" stroke="#fff" stroke-width="3" fill="none"/></svg></div>
  </article>
  <article class="type-card abs" style="left:660px">
    <div class="thumb" role="img" aria-label="Electrician fitting a pendant light in a home" style="background:linear-gradient(135deg,#b87a5a,#5a3a2c)"></div>
    <h3>Home Owner</h3>
    <p>Lorem ipsum dolor sit amet, consectetur adipiscing elit. Duis egestas sapien non libero eleifend facilisis. Donec consectetur aliquam tortor, nec viverra magna dictum nec.</p>
    <div class="more">Read More <svg width="22" height="18" viewBox="0 0 22 18"><path d="M2 9h16M12 3l6 6-6 6" stroke="#fff" stroke-width="3" fill="none"/></svg></div>
  </article>
</section>

<section class="newsletter abs">
  <h3>Join Our Newsletter</h3>
  <div class="field">Enter The Email</div>
  <div class="cta">Subscribe Now</div>
</section>

<footer class="site-footer abs">
  <div class="brand"><span class="brand-dot"></span>Brightway Systems</div>
  <div class="foot-col" style="left:411px"><h4>Quick Links</h4><ul><li>Home</li><li>Meet The Team</li><li>Our Services</li><li>Projects</li><li>Contact Us</li></ul></div>
  <div class="foot-col" style="left:639px"><h4>Services</h4><ul><li>Business</li><li>House owner</li></ul></div>
  <div class="foot-col" style="left:819px"><h4>Contact Us</h4><ul><li>01632 960418</li><li>12 Harbour Row, Seaford, BN25 4QT</li><li>info@brightwaysystems.co.uk</li></ul></div>
  <div class="foot-bottom"><span>© 2019 Brightway All right reserved Term of Use</span><div class="social"><span></span><span></span><span></span><span></span></div></div>
</footer>

</body>
</html>
```